Harbor Oak Electric website

I need a website for my electrical service business. We do a variety of electrical services for both commercial and residential clients in the Raleigh/Durham area of NC. I would like it to be done by someone who understands the electrical trade. I want a design that uses the color green in my logo. The design should communicate quality in electrical services for jobs big and small. It should have a button to call and a section to email requesting services. A place to list the time of services we offer as well. mobile friendly. First page should have a section for testimonials. A list of services will be provided. Only clean clear pictures. I will provide some.

```html
<!DOCTYPE html>
<html lang="en">
<head>
<meta charset="utf-8">
<title>Harbor Oak Electric</title>
<link href="https://fonts.googleapis.com/css2?family=Michroma&family=Roboto:ital,wght@0,400;0,500;0,700;1,700&display=swap" rel="stylesheet">
<style>
:root{
  --green:#12a04b;
  --green-dark:#0b8a3d;
  --ink:#1d1d1d;
  --dark:#1f1f1f;
  --text:#6f6f6f;
  --light:#f3f3f3;
  --white:#fff;
  --star:#f5b400;
}
*{box-sizing:border-box;margin:0;padding:0}
html,body{width:1200px;height:4422px;overflow:hidden}
body{font-family:'Roboto',sans-serif;color:var(--ink);background:var(--white);position:relative}
.abs{position:absolute}
.display{font-family:'Michroma',sans-serif;font-weight:400;letter-spacing:2px;text-transform:uppercase}
.brand{font-family:'Roboto',sans-serif;font-weight:700;text-transform:uppercase;line-height:1.1;letter-spacing:1px}

/* header */
.site-header{top:0;left:0;width:1200px;height:84px;background:var(--white)}
.site-header .brand{left:110px;top:22px;font-size:18px;color:var(--ink)}
.site-header .brand small{display:block;font-size:11px;letter-spacing:6px}
.nav{top:33px;display:flex;font-size:14px;font-weight:500}
.nav a{position:absolute;color:var(--ink);text-decoration:none;white-space:nowrap}
.consult{left:893px;top:0;width:307px;height:84px;background:var(--green);color:var(--white)}
.consult .ring{left:-2px;top:20px;width:46px;height:46px;border-radius:50%;background:var(--ink);border:3px solid var(--white)}
.consult .label{left:63px;top:21px;font-size:12px;font-weight:500}
.consult .num{left:63px;top:38px;font-size:18px;font-weight:700}

/* hero */
.hero{top:84px;left:0;width:1200px;height:706px;background:linear-gradient(100deg,#6f6a63 0%,#a8a49c 30%,#d9d6d0 55%,#2c3350 75%,#c9c6c0 100%);overflow:hidden}
.hero-shade{inset:0;background:linear-gradient(90deg,rgba(0,0,0,.45),rgba(0,0,0,.1) 55%,rgba(0,0,0,0))}
.hero-title{left:110px;top:198px;font-size:40px;color:var(--white)}
.hero-text{left:110px;top:262px;width:460px;font-size:16px;line-height:26px;color:var(--white)}
.hero-btn{left:117px;top:346px;width:261px;height:47px;background:var(--green);color:var(--white);font-size:15px;font-weight:700;display:flex;align-items:center;justify-content:center;gap:8px;clip-path:polygon(6% 0,100% 0,94% 100%,0 100%)}
.hero-cut{left:0;top:576px;width:1200px;height:130px}

/* about */
.about-photo{left:110px;top:888px;width:453px;height:417px;background:linear-gradient(135deg,#2f3b4f,#8b8f95 50%,#c8c49a)}
.about-card{left:297px;top:1250px;width:266px;height:124px;background:var(--white);padding:18px 31px}
.about-card p{font-size:15px;font-weight:500;line-height:25px}
.btn-sm{display:inline-flex;align-items:center;justify-content:center;gap:7px;color:var(--white);font-size:13px;font-weight:700;text-transform:uppercase}
.about-card .btn-sm{margin-top:10px;width:208px;height:40px;background:var(--green);border-radius:3px}
.eyebrow{font-size:14px;font-weight:700;color:var(--green);text-transform:uppercase}
.about-copy{left:634px;top:922px;width:450px}
.about-copy h2{font-size:32px;margin-top:10px}
.about-copy p{font-size:13.5px;line-height:27px;color:var(--text);margin-top:18px}
.read-more{left:634px;top:1250px;width:166px;height:45px;background:var(--green);clip-path:polygon(6% 0,100% 0,94% 100%,0 100%)}
.call-today{left:827px;top:1253px}
.call-today .ico{left:0;top:2px;width:38px;height:38px;border-radius:50%;background:var(--green)}
.call-today .lbl{left:55px;top:0;font-size:12px;color:var(--ink);white-space:nowrap}
.call-today .num{left:55px;top:18px;font-size:20px;font-weight:700;color:var(--green);white-space:nowrap}

/* split */
.split{left:0;top:1447px;width:1200px;height:533px}
.split-col{top:112px;width:370px;color:var(--white)}
.split-col .badge{width:82px;height:82px;border-radius:50%;background:var(--white);display:flex;align-items:center;justify-content:center}
.split-col h3{font-size:22px;margin-top:36px}
.split-col p{font-size:14px;line-height:25px;margin-top:14px}
.split-col .more{margin-top:22px;font-size:14px;font-weight:700;display:flex;align-items:center;gap:7px}

/* services */
.section-title{left:0;width:1200px;text-align:center;font-size:36px}
.tabs{left:438px;top:2088px;display:flex;gap:6px}
.tab{width:160px;height:43px;display:flex;align-items:center;justify-content:center;color:var(--white);font-size:13px;font-weight:700;clip-path:polygon(8% 0,100% 0,92% 100%,0 100%)}
.tab.on{background:var(--green)}.tab.off{background:var(--ink)}
.cards{left:112px;top:2187px;display:flex;gap:15px}
.card{width:233px;height:306px;background:var(--white);box-shadow:0 4px 16px rgba(0,0,0,.12);position:relative;text-align:center}
.card .pic{height:153px}
.card .hex{position:absolute;left:89px;top:126px}
.card h4{font-size:16px;font-weight:500;margin-top:56px}
.card p{font-size:13px;line-height:20px;color:var(--text);padding:8px 18px 0}

/* why */
.why-title{left:110px;top:2672px;font-size:28px}
.why-list{left:110px;top:2750px;list-style:none}
.why-list li{display:flex;align-items:center;gap:22px;height:45.5px;font-size:16px;color:#444}
.why-photo{left:599px;top:2615px;width:490px;height:419px;background:linear-gradient(120deg,#9aa0a4,#d6d7d4 40%,#e8862a 62%,#6d6f6c)}

/* testimonials */
.testi{left:0;top:3159px;width:1200px;height:540px;background:var(--light)}
.tcard{top:3338px;width:310px;height:190px;background:var(--white);border-top:3px solid var(--green);border-radius:10px;box-shadow:0 4px 14px rgba(0,0,0,.08);text-align:center;padding:68px 26px 0}
.tcard p{font-size:13.5px;line-height:26px;color:var(--text)}
.tcard .avatar{left:109px;top:-45px;width:92px;height:92px;border-radius:50%;background:linear-gradient(#cfcfcf,#8c8c8c);border:3px solid var(--white)}
.tcard .pointer{left:145px;bottom:-10px;width:20px;height:20px;background:var(--white);transform:rotate(45deg)}
.tname{top:3552px;width:310px;text-align:center;font-size:14px;font-weight:500}
.tname small{font-size:9px;font-weight:400}
.stars{top:3576px;width:310px;text-align:center;color:var(--star);font-size:12px;letter-spacing:1px}

/* cta */
.cta{left:0;top:3623px;width:1200px;height:412px;background:var(--green);clip-path:polygon(0 0,100% 30px,100% 100%,0 100%)}
.cta-title{left:0;top:3778px;width:1200px;text-align:center;font-size:29px;line-height:38px;color:var(--white)}
.cta-phone{left:276px;top:3880px;color:var(--white)}
.cta-phone .ico{left:0;top:8px;width:42px;height:42px;border-radius:50%;border:2px solid var(--white)}
.cta-phone .lbl{left:58px;top:0;font-size:16px;font-weight:500;white-space:nowrap}
.cta-phone .num{left:58px;top:20px;font-size:32px;white-space:nowrap}
.cta-phone .num b{font-weight:700}
.cta-or{left:632px;top:3862px}
.cta-btn{left:755px;top:3890px;width:205px;height:47px;background:var(--ink);border-radius:3px}

/* footer */
.footer{left:0;top:4035px;width:1200px;height:387px;background:var(--dark);color:var(--white)}
.footer .brand{left:110px;top:92px;font-size:18px}
.footer .brand small{display:block;font-size:11px;letter-spacing:6px}
.footer .about{left:110px;top:158px;width:240px;font-size:12.5px;line-height:19px}
.socials{left:110px;top:237px;display:flex;gap:8px}
.socials span{width:30px;height:30px;border-radius:50%;background:var(--green)}
.fcol{top:78px}
.fcol h5{font-size:16px;font-weight:700;margin-bottom:22px}
.fcol li{list-style:none;font-size:12.5px;line-height:25.5px}
.contact-item{position:relative;padding-left:22px;font-size:12.5px;line-height:18px;margin-bottom:14px}
.contact-item b{font-size:11px;display:block}
.contact-item svg{position:absolute;left:0;top:2px}
.fdivider{left:110px;top:314px;width:979px;height:1px;background:#3a3a3a}
.copy{left:0;top:343px;width:1200px;text-align:center;font-size:13px}
.to-top{left:1133px;top:263px;width:34px;height:34px;border-radius:50%;background:var(--green)}
</style>
</head>
<body>

<header class="site-header abs">
  <div class="brand abs">Harbor Oak<small>Electric</small></div>
  <nav class="nav abs" style="left:0">
    <a style="left:410px">Home</a>
    <a style="left:482px">About Us</a>
    <a style="left:575px">Services</a>
    <a style="left:666px">Testimonial</a>
    <a style="left:778px">Contact Us</a>
  </nav>
  <div class="consult abs">
    <div class="ring abs"><svg width="40" height="40" viewBox="0 0 40 40"><path d="M14 11c1-1 2-1 3 0l2 3c1 1 0 2-1 3l-1 1c1 2 3 4 5 5l1-1c1-1 2-2 3-1l3 2c1 1 1 2 0 3l-2 2c-6 0-15-9-15-15z" fill="#fff"/></svg></div>
    <div class="label abs">Free Consultation</div>
    <div class="num abs">(919) 555-0100</div>
  </div>
</header>

<section class="hero abs">
  <div class="abs" style="inset:0" role="img" aria-label="Bright modern kitchen with white cabinets and a navy island"></div>
  <div class="hero-shade abs"></div>
  <h1 class="hero-title display abs">Harbor Oak</h1>
  <p class="hero-text abs">Lorem ipsum dolor sit amet, consectetur adipiscing elit, eiusmod tempor incididunt ut magna aliqua.</p>
  <div class="hero-btn abs">REQUESTING SERVICES <svg width="14" height="14" viewBox="0 0 14 14"><circle cx="7" cy="7" r="7" fill="#fff"/><path d="M5.5 4l3 3-3 3" stroke="#12a04b" stroke-width="2" fill="none"/></svg></div>
  <svg class="hero-cut abs" viewBox="0 0 1200 130" preserveAspectRatio="none">
    <polygon points="0,0 620,108 1200,80 1200,130 0,130" fill="#fff"/>
    <polygon points="420,65 620,108 1200,30 1200,80 620,108 600,122" fill="#12a04b"/>
    <polygon points="600,104 620,122 1200,80 1200,30" fill="#12a04b"/>
  </svg>
</section>

<section>
  <div class="about-photo abs" role="img" aria-label="Electrician working on a wiring panel"></div>
  <div class="about-card abs">
    <p>Have a Electric Repair?<br>Contact Our Friendly Team!</p>
    <div class="btn-sm">Schedule a Service <svg width="13" height="13" viewBox="0 0 14 14"><circle cx="7" cy="7" r="7" fill="#fff"/><path d="M5.5 4l3 3-3 3" stroke="#12a04b" stroke-width="2" fill="none"/></svg></div>
  </div>
  <div class="about-copy abs">
    <div class="eyebrow">About Us</div>
    <h2 class="display">Harbor Oak</h2>
    <p>Lorem ipsum dolor sit amet, consectetur adipiscing elit, sed do eiusmod tempor incididunt ut labore et dolore magna aliqua. Ut enim ad minim veniam, quis nostrud exercitation ullamco laboris nisi ut aliquip ex ea commodo consequat.</p>
    <p>Duis aute irure dolor in reprehenderit in voluptate velit esse cillum dolore eu fugiat nulla pariatur. Excepteur sint occaecat cupidatat non proident, sunt in culpa qui officia id est laborum.</p>
  </div>
  <div class="read-more abs btn-sm">Read More <svg width="13" height="13" viewBox="0 0 14 14"><circle cx="7" cy="7" r="7" fill="#fff"/><path d="M5.5 4l3 3-3 3" stroke="#12a04b" stroke-width="2" fill="none"/></svg></div>
  <div class="call-today abs">
    <div class="ico abs"><svg width="38" height="38" viewBox="0 0 40 40"><path d="M14 11c1-1 2-1 3 0l2 3c1 1 0 2-1 3l-1 1c1 2 3 4 5 5l1-1c1-1 2-2 3-1l3 2c1 1 1 2 0 3l-2 2c-6 0-15-9-15-15z" fill="#fff"/></svg></div>
    <div class="lbl abs">Call Us Today</div>
    <div class="num abs">919-555-0142</div>
  </div>
</section>

<section class="split abs">
  <svg class="abs" style="left:0;top:0" width="1200" height="533" viewBox="0 0 1200 533">
    <polygon points="0,0 555,62 520,255 600,245 560,490 0,533" fill="#12a04b"/>
    <polygon points="655,62 1200,0 1200,533 595,485 640,292 580,302" fill="#1d1d1d"/>
  </svg>
  <div class="split-col abs" style="left:112px">
    <div class="badge"><svg width="42" height="42" viewBox="0 0 42 42" fill="none" stroke="#12a04b" stroke-width="2"><rect x="8" y="12" width="12" height="26"/><rect x="22" y="6" width="12" height="32"/><path d="M4 38h34M12 17h4M12 23h4M12 29h4M26 12h4M26 18h4M26 24h4M26 30h4"/></svg></div>
    <h3 class="display">Commercial</h3>
    <p>Lorem ipsum dolor sit amet, consectetur adipiscing elit, sed do eiusmod tempor incididunt ut labore et dolore magna aliqua. Ut enim ad minim veniam, quis nostrud ut aliquip ex ea commodo consequat.</p>
    <div class="more">LEARN MORE <svg width="13" height="13" viewBox="0 0 14 14"><circle cx="7" cy="7" r="7" fill="#fff"/><path d="M5.5 4l3 3-3 3" stroke="#12a04b" stroke-width="2" fill="none"/></svg></div>
  </div>
  <div class="split-col abs" style="left:748px">
    <div class="badge"><svg width="42" height="42" viewBox="0 0 42 42" fill="none" stroke="#12a04b" stroke-width="2"><path d="M5 20L21 7l16 13M9 17v20h24V17M17 37V27h8v10"/></svg></div>
    <h3 class="display">Residential</h3>
    <p>Lorem ipsum dolor sit amet, consectetur adipiscing elit, sed do eiusmod tempor incididunt ut labore et dolore magna aliqua. Ut enim ad minim veniam, quis nostrud ut aliquip ex ea commodo consequat.</p>
    <div class="more">LEARN MORE <svg width="13" height="13" viewBox="0 0 14 14"><circle cx="7" cy="7" r="7" fill="#fff"/><path d="M5.5 4l3 3-3 3" stroke="#1d1d1d" stroke-width="2" fill="none"/></svg></div>
  </div>
</section>

<section>
  <h2 class="section-title display abs" style="top:2025px">What We Do</h2>
  <div class="tabs abs"><div class="tab on">RESIDENTIAL</div><div class="tab off">COMMERCIAL</div></div>
  <div class="cards abs">
    <article class="card"><div class="pic" role="img" aria-label="Renovated living room" style="background:linear-gradient(135deg,#8a8178,#d8d2c8)"></div>
      <svg class="hex" width="56" height="60" viewBox="0 0 56 60"><polygon points="28,2 54,16 54,44 28,58 2,44 2,16" fill="#12a04b" stroke="#fff" stroke-width="3"/><path d="M18 30l10-9 10 9M21 28v11h14V28" stroke="#fff" stroke-width="2" fill="none"/></svg>
      <h4>Remodels</h4><p>Lorem ipsum dolor consectetur adipiscing elit, sed do eiusmod tempor incididunt</p></article>
    <article class="card"><div class="pic" role="img" aria-label="House framing under construction" style="background:linear-gradient(135deg,#b88a52,#e6d3b4)"></div>
      <svg class="hex" width="56" height="60" viewBox="0 0 56 60"><polygon points="28,2 54,16 54,44 28,58 2,44 2,16" fill="#12a04b" stroke="#fff" stroke-width="3"/><path d="M19 40V22h18v18M23 26h10M23 31h10M23 36h10" stroke="#fff" stroke-width="2" fill="none"/></svg>
      <h4>New Construction</h4><p>Lorem ipsum dolor consectetur adipiscing elit, sed do eiusmod tempor incididunt</p></article>
    <article class="card"><div class="pic" role="img" aria-label="Technicians beside outdoor HVAC units" style="background:linear-gradient(135deg,#6c7a86,#c4cbd0 60%,#e08a3a)"></div>
      <svg class="hex" width="56" height="60" viewBox="0 0 56 60"><polygon points="28,2 54,16 54,44 28,58 2,44 2,16" fill="#12a04b" stroke="#fff" stroke-width="3"/><rect x="18" y="22" width="20" height="16" stroke="#fff" stroke-width="2" fill="none"/><circle cx="28" cy="30" r="5" stroke="#fff" stroke-width="2" fill="none"/></svg>
      <h4>Hvac And Heatpumps</h4><p>Lorem ipsum dolor consectetur adipiscing elit, sed do eiusmod tempor incididunt</p></article>
    <article class="card"><div class="pic" role="img" aria-label="Electrician installing solar equipment" style="background:linear-gradient(135deg,#9ea3a0,#dedcd2 55%,#b9c56a)"></div>
      <svg class="hex" width="56" height="60" viewBox="0 0 56 60"><polygon points="28,2 54,16 54,44 28,58 2,44 2,16" fill="#12a04b" stroke="#fff" stroke-width="3"/><path d="M20 24h18l-3 12H17zM23 24l-3 12M29 24l-3 12M35 24l-3 12M18 30h19" stroke="#fff" stroke-width="1.6" fill="none"/></svg>
      <h4>Alternative Power</h4><p>Lorem ipsum dolor consectetur adipiscing elit, sed do eiusmod tempor incididunt</p></article>
  </div>
</section>

<section>
  <h2 class="why-title display abs">Why Choose Us?</h2>
  <ul class="why-list abs">
    <li><svg width="32" height="32" viewBox="0 0 32 32"><rect x="3" y="6" width="26" height="23" rx="2" fill="none" stroke="#12a04b" stroke-width="2"/><rect x="3" y="6" width="26" height="6" fill="#12a04b"/></svg>Servicing the Triangle 24-7-365</li>
    <li><svg width="32" height="32" viewBox="0 0 32 32"><circle cx="16" cy="11" r="7" fill="none" stroke="#12a04b" stroke-width="2"/><path d="M5 26c4-4 8-4 11-2s7 2 11-2" stroke="#12a04b" stroke-width="2" fill="none"/></svg>Cost Effective Options Available</li>
    <li><svg width="32" height="32" viewBox="0 0 32 32"><path d="M4 28h24M8 28V14h8v14M18 28V8h8v20" stroke="#12a04b" stroke-width="2" fill="none"/></svg>Focus on remodels and new construction</li>
    <li><svg width="32" height="32" viewBox="0 0 32 32"><circle cx="16" cy="16" r="12" fill="none" stroke="#12a04b" stroke-width="2"/><path d="M16 9v7l5 3" stroke="#12a04b" stroke-width="2" fill="none"/></svg>Call or Chat with us Anytime</li>
    <li><svg width="32" height="32" viewBox="0 0 32 32"><path d="M9 16l5 5 10-11" stroke="#12a04b" stroke-width="3" fill="none"/></svg>100% Satisfaction Guarantee</li>
  </ul>
  <div class="why-photo abs" role="img" aria-label="Smiling electrician in a hard hat with a laptop at a control panel"></div>
</section>

<section>
  <div class="testi abs"></div>
  <h2 class="section-title display abs" style="top:3213px;font-size:32px">What Our Clients Say</h2>
  <div class="tcard abs" style="left:112px"><div class="avatar abs" role="img" aria-label="Client portrait"></div><p>Sed ut perspiciatis unde omnis iste natus error sit voluptatem accusantium doloremque laudantium, totam rem aperiam, eaque ipsa</p><div class="pointer abs"></div></div>
  <div class="tcard abs" style="left:445px"><div class="avatar abs" role="img" aria-label="Client portrait"></div><p>Sed ut perspiciatis unde omnis iste natus error sit voluptatem accusantium doloremque laudantium, totam rem aperiam, eaque ipsa</p><div class="pointer abs"></div></div>
  <div class="tcard abs" style="left:779px"><div class="avatar abs" role="img" aria-label="Client portrait"></div><p>Sed ut perspiciatis unde omnis iste natus error sit voluptatem accusantium doloremque laudantium, totam rem aperiam, eaque ipsa</p><div class="pointer abs"></div></div>
  <div class="tname abs" style="left:112px">Dana Whitfield, <small>Chairman RDC</small></div>
  <div class="tname abs" style="left:445px">Lena Marsh, <small>Project Manager</small></div>
  <div class="tname abs" style="left:779px">Owen Pratt, <small>Chairman RDC</small></div>
  <div class="stars abs" style="left:112px">★★★★★</div>
  <div class="stars abs" style="left:445px">★★★★★</div>
  <div class="stars abs" style="left:779px">★★★★★</div>
</section>

<section>
  <div class="cta abs"></div>
  <h2 class="cta-title display abs">Day or Nigh, 24/7, Count on Trusted<br>Sercice from Harbor Oak</h2>
  <div class="cta-phone abs">
    <div class="ico abs"><svg width="38" height="38" viewBox="0 0 40 40"><path d="M14 11c1-1 2-1 3 0l2 3c1 1 0 2-1 3l-1 1c1 2 3 4 5 5l1-1c1-1 2-2 3-1l3 2c1 1 1 2 0 3l-2 2c-6 0-15-9-15-15z" fill="#fff"/></svg></div>
    <div class="lbl abs">Need help now?</div>
    <div class="num abs">Call: <b>919-555-0188</b></div>
  </div>
  <svg class="cta-or abs" width="120" height="70" viewBox="0 0 120 70"><path d="M4 24C30 6 70 4 118 18" stroke="#fff" stroke-width="2" fill="none"/><path d="M110 12l8 6-9 4" stroke="#fff" stroke-width="2" fill="none"/><text x="42" y="56" fill="#fff" font-family="Roboto,sans-serif" font-style="italic" font-weight="700" font-size="28">or</text></svg>
  <div class="cta-btn abs btn-sm">Schedule Service <svg width="13" height="13" viewBox="0 0 14 14"><circle cx="7" cy="7" r="7" fill="#fff"/><path d="M5.5 4l3 3-3 3" stroke="#1d1d1d" stroke-width="2" fill="none"/></svg></div>
</section>

<footer class="footer abs">
  <div class="brand abs">Harbor Oak<small>Electric</small></div>
  <p class="about abs">We are fully licensed and insured and are 100% legal and town approved our system exceeds all local building</p>
  <div class="socials abs"><span></span><span></span><span></span><span></span></div>
  <div class="fcol abs" style="left:434px"><h5>Quick Links</h5><ul><li>Home</li><li>About Us</li><li>Services</li><li>Testimonial</li><li>Contact Us</li></ul></div>
  <div class="fcol abs" style="left:646px"><h5>About Company</h5><ul><li>Terms of Use</li><li>Terms &amp; Condition</li><li>News</li><li>Privacy Policy</li><li>FAQ</li></ul></div>
  <div class="fcol abs" style="left:870px;width:230px"><h5>Contact Us</h5>
    <div class="contact-item"><svg width="10" height="13" viewBox="0 0 10 13"><path d="M5 0a5 5 0 015 5c0 3-5 8-5 8S0 8 0 5a5 5 0 015-5z" fill="#12a04b"/><circle cx="5" cy="5" r="2" fill="#1f1f1f"/></svg><b>Location</b>2418 Lorem ipsum dolor amet, consectetur adipiscing elit</div>
    <div class="contact-item"><svg width="12" height="12" viewBox="0 0 40 40"><path d="M8 4c2-2 4-2 6 0l4 6c1 2 0 4-2 5l-2 2c2 4 6 8 10 10l2-2c1-2 3-3 5-2l6 4c2 2 2 4 0 6l-4 4C20 37 3 20 4 8z" fill="#12a04b"/></svg><b>Phone</b>(919) 555 – 0142</div>
    <div class="contact-item"><svg width="12" height="10" viewBox="0 0 12 10"><rect width="12" height="10" fill="#12a04b"/><path d="M0 0l6 5 6-5" stroke="#1f1f1f" fill="none"/></svg><b>Email</b>info@harboroakelectric.com</div>
  </div>
  <div class="to-top abs"><svg width="34" height="34" viewBox="0 0 34 34"><path d="M11 20l6-6 6 6" stroke="#fff" stroke-width="2" fill="none"/></svg></div>
  <div class="fdivider abs"></div>
  <div class="copy abs">2021 Copyright - Harbor Oak Electric &nbsp;| All Rights Reserved</div>
</footer>

</body>
</html>
```